presentation slide template in Adobe Indesign

Hi, we need to design a template for presentation slides as well as presentation-like documents in slide format. See our website: halvmere-consulting.com and also graphical profile attached as a file. I've also attached the images used on our web site.
Regards,
Anselm
Updates
Hi, a clarification: this is about a presentation template not a specific presentation based on the web site content. I only supplied the web site for you as a reference. I imagine the result would include a base slide template that can be used for the bulk of the slides in a presentation and then a number of template slides that can be inserted in to a presentation to make it visually more interesting.
Target Market(s)
Management Consulting, Financial Risk Advisory
Requirements
Must have
- End product must be an Adobe InDesign template.

```html
<!DOCTYPE html>
<html lang="en">
<head>
<meta charset="utf-8">
<title>Halvmere Consulting – Slide Template Set</title>
<link href="https://fonts.googleapis.com/css2?family=Arvo&display=swap" rel="stylesheet">
<style>
  :root {
    --slate: #4b6064;
    --slate-soft: rgba(75, 96, 100, 0.72);
    --white: #ffffff;
    --ink: #1e1e1e;
    --panel: rgba(255, 255, 255, 0.9);
    --steel-dark: #2e3439;
    --steel-mid: #6f7a84;
    --steel-light: #b9c1c8;
    --sky-teal: #8fa9a6;
    --sky-haze: #c9c8b4;
    --sky-warm: #ddd1a8;
  }
  * { margin: 0; padding: 0; box-sizing: border-box; }
  html, body { width: 1200px; height: 300px; overflow: hidden; background: var(--white); }
  body { font-family: "Arvo", Georgia, serif; display: flex; }

  .slide { position: relative; width: 400px; height: 300px; overflow: hidden; }

  .photo { position: absolute; inset: 0; }
  .photo--turbine {
    background:
      radial-gradient(ellipse at 80% 50%, var(--steel-dark) 0%, transparent 45%),
      linear-gradient(100deg, var(--steel-light) 0%, var(--steel-mid) 40%, var(--steel-light) 62%, var(--steel-mid) 85%, var(--steel-dark) 100%);
  }
  .photo--kites {
    background:
      radial-gradient(ellipse at 85% 10%, #e9ecea 0%, transparent 35%),
      linear-gradient(180deg, var(--sky-teal) 0%, var(--sky-haze) 60%, var(--sky-warm) 100%);
  }

  /* Cover slide */
  .cover-band {
    position: absolute; left: 0; top: 120px; width: 400px; height: 62px;
    background: var(--slate-soft);
  }
  .cover-mark {
    position: absolute; left: 134px; top: 122px; width: 140px; height: 60px;
    background: var(--white);
    display: flex; flex-direction: column; justify-content: center; align-items: center;
  }

  .brand { color: var(--ink); text-transform: uppercase; line-height: 1.1; text-align: center; }
  .brand span { display: block; }
  .brand--large { font-size: 12.5px; letter-spacing: 0.04em; }
  .brand--large span + span { letter-spacing: 0.24em; font-size: 10px; }
  .brand--small { font-size: 8px; letter-spacing: 0.02em; }
  .brand--small span + span { letter-spacing: 0.2em; font-size: 6.5px; }

  .footer-mark { position: absolute; right: 16px; bottom: 10px; }

  /* Content slide */
  .title-bar {
    position: absolute; left: 0; top: 17px; width: 240px; height: 39px;
    background: var(--slate);
    color: var(--white); font-size: 15px;
    display: flex; align-items: center; padding-left: 12px;
    text-transform: uppercase;
  }

  /* Feature slide */
  .feature-head {
    position: absolute; left: 51px; top: 48px; width: 304px; height: 34px;
    background: var(--slate);
  }
  .feature-body {
    position: absolute; left: 51px; top: 82px; width: 304px; height: 171px;
    background: var(--panel);
  }
</style>
</head>
<body>
  <section class="slide slide--cover">
    <div class="photo photo--turbine" role="img" aria-label="Close-up photograph of turbine blades in cool steel tones"></div>
    <div class="cover-band"></div>
    <div class="cover-mark">
      <p class="brand brand--large"><span>Halvmere</span><span>Consulting</span></p>
    </div>
  </section>

  <section class="slide slide--content">
    <h1 class="title-bar">Slide Title</h1>
    <p class="brand brand--small footer-mark"><span>Halvmere</span><span>Consulting</span></p>
  </section>

  <section class="slide slide--feature">
    <div class="photo photo--kites" role="img" aria-label="Photograph of colourful kites flying against a hazy sky"></div>
    <div class="feature-head"></div>
    <div class="feature-body"></div>
    <p class="brand brand--small footer-mark"><span>Halvmere</span><span>Consulting</span></p>
  </section>
</body>
</html>
```